Construction Directory Website Flyer

We need a postcard size +/- or somewhere around that size (something standard) flyer designed for our construction directory website. Leave a spot for tagline. Call to action is 'register your company now'. I am thinking many mini pictures of different construction to show that it is for the entire construction industry. Logo and screenshot of the homepage of the website is attached. Use same theme as webpage.

Target Market(s)

Construction Industry

Industry/Entity Type

Construction

Font styles to use
Sans Serif

Requirements
Must have
• Call to action
• Colors to match logo
• Area to add description and details.
Nice to have
• Construction Images
Should not have
• No Cartoonish types of things

```html
<!DOCTYPE html>
<html lang="en">
<head>
<meta charset="utf-8">
<title>BuildLink Hub Flyer</title>
<link href="https://fonts.googleapis.com/css2?family=Bebas+Neue&family=Ubuntu:wght@400;500&display=swap" rel="stylesheet">
<style>
  :root {
    --backdrop: #86a3a3;
    --paper: #f1f1f1;
    --slate: #4e5d6c;
    --slate-dark: #3d4a57;
    --orange: #e8762b;
    --red: #e2362a;
    --ink: #3a4550;
    --white: #ffffff;
  }
  * { margin: 0; padding: 0; box-sizing: border-box; }
  html, body { width: 1200px; height: 960px; overflow: hidden; }
  body {
    background: var(--backdrop);
    font-family: "Ubuntu", sans-serif;
    position: relative;
  }
  .flyer {
    position: absolute;
    left: 285px;
    top: 35px;
    width: 630px;
    height: 890px;
    background: var(--paper);
    overflow: hidden;
    box-shadow: 0 10px 30px rgba(0,0,0,0.25);
  }
  .flyer-art { position: absolute; inset: 0; }
  .brand {
    position: absolute;
    top: 52px;
    left: 0;
    width: 100%;
    display: flex;
    justify-content: center;
    align-items: center;
    gap: 16px;
  }
  .brand-square {
    width: 58px;
    height: 58px;
    background: var(--slate);
  }
  .brand-name {
    font-family: "Ubuntu", sans-serif;
    font-weight: 500;
    font-size: 32px;
    line-height: 1.05;
    color: var(--ink);
  }
  .cta {
    position: absolute;
    left: 30px;
    top: 708px;
    font-family: "Bebas Neue", sans-serif;
    font-size: 38px;
    letter-spacing: 0.5px;
    color: var(--orange);
  }
  .contact-list {
    position: absolute;
    left: 30px;
    top: 760px;
    list-style: none;
  }
  .contact-item {
    display: flex;
    align-items: center;
    gap: 10px;
    height: 25px;
    font-size: 19px;
    color: var(--white);
  }
  .contact-icon { width: 20px; height: 20px; flex: none; }
</style>
</head>
<body>
  <main class="flyer">
    <svg class="flyer-art" width="630" height="890" viewBox="0 0 630 890">
      <defs>
        <linearGradient id="skyTone" x1="0" y1="0" x2="1" y2="1">
          <stop offset="0" stop-color="#0e1a2c"/>
          <stop offset="0.45" stop-color="#2b5a93"/>
          <stop offset="1" stop-color="#1d3a63"/>
        </linearGradient>
        <radialGradient id="sunGlow" cx="0.3" cy="0.75" r="0.5">
          <stop offset="0" stop-color="#f6a531" stop-opacity="0.95"/>
          <stop offset="1" stop-color="#f6a531" stop-opacity="0"/>
        </radialGradient>
        <linearGradient id="slateFade" x1="0" y1="0" x2="0" y2="1">
          <stop offset="0" stop-color="var(--slate-dark)"/>
          <stop offset="1" stop-color="var(--slate)"/>
        </linearGradient>
      </defs>
      <polygon class="info-panel" points="0,548 630,700 630,890 0,890" fill="url(#slateFade)"/>
      <g class="hero-photo" role="img" aria-label="Photograph of an industrial plant with steel tower, pipelines and a gas flare against a sunset sky">
        <polygon points="31,228 143,168 630,278 630,730 68,563" fill="url(#skyTone)"/>
        <polygon points="31,228 143,168 630,278 630,730 68,563" fill="url(#sunGlow)"/>
      </g>
      <g class="tagline-band">
        <polygon points="233,148 630,208 630,278 203,183" fill="var(--orange)"/>
        <polygon points="233,148 380,170 350,205 203,183" fill="var(--red)" opacity="0.6"/>
        <text x="250" y="180" transform="rotate(8 250 180)" font-family="Bebas Neue, sans-serif" font-size="25" fill="#ffffff" letter-spacing="0.5">BUILT BY CONSTRUCTION FOR CONSTRUCTION</text>
      </g>
    </svg>

    <header class="brand">
      <span class="brand-square"></span>
      <span class="brand-name">BuildLink<br>Hub</span>
    </header>

    <h2 class="cta">Register Your Company Now</h2>

    <ul class="contact-list">
      <li class="contact-item">
        <svg class="contact-icon" viewBox="0 0 20 20"><circle cx="10" cy="10" r="8.5" fill="none" stroke="var(--orange)" stroke-width="1.6"/><rect x="7" y="5" width="6" height="10" rx="1" fill="none" stroke="var(--orange)" stroke-width="1.4"/></svg>
        (000) 123-4567
      </li>
      <li class="contact-item">
        <svg class="contact-icon" viewBox="0 0 20 20"><circle cx="10" cy="10" r="9" fill="var(--orange)"/><rect x="5" y="6.5" width="10" height="7" fill="none" stroke="#fff" stroke-width="1.3"/><polyline points="5,6.5 10,10.5 15,6.5" fill="none" stroke="#fff" stroke-width="1.3"/></svg>
        info@buildlinkhub.com
      </li>
      <li class="contact-item">
        <svg class="contact-icon" viewBox="0 0 20 20"><circle cx="10" cy="10" r="9" fill="var(--orange)"/><polygon points="7,5 14,11 10.5,11.5 12.5,15 11,15.6 9.2,12.2 7,14.5" fill="#fff"/></svg>
        www.buildlinkhub.com
      </li>
      <li class="contact-item">
        <svg class="contact-icon" viewBox="0 0 20 20"><circle cx="10" cy="10" r="8.5" fill="none" stroke="var(--orange)" stroke-width="1.6"/><path d="M10 15 C7 11 6.5 9.5 6.5 8.5 A3.5 3.5 0 0 1 13.5 8.5 C13.5 9.5 13 11 10 15 Z" fill="var(--orange)"/><circle cx="10" cy="8.5" r="1.3" fill="var(--slate)"/></svg>
        Dummy dummy, st suite, Zipcode 12345
      </li>
    </ul>
  </main>
</body>
</html>
```